Brimble Diecast Torvel Collectables Website

looking for a vibrant web site marketplace built for diecast car enthusiasts to buy, sell, and trade with ease. Whether you're looking to showcase your own collection or discover rare and exciting models, our site makes the process simple and enjoyable. Clients can browse a curated inventory of high‑quality diecast cars, connect with fellow collectors, and find the perfect pieces to expand their collection. With a smooth user experience and a community-driven spirit, we’re the go‑to destination for anyone passionate about diecast cars.

Target Market(s)

diecast collectors

Industry/Entity Type

Diecast Collectables

Coding

Coded - Design and coding required

Number of Pages Required

3 page

Font styles to use
Sans Serif

Colors
EE7325
F08F49
F5BC92
FAE3D3
FDF4ED

Requirements
Must have
• Cool look and feel. Woo commerce page to post and sell my inventory
Nice to have
• page for users to post their cars or looking for trades.
Should not have
• look cheap

```html
<!DOCTYPE html>
<html lang="en">
<head>
<meta charset="utf-8">
<title>Brimble Diecast — Home & Marketplace</title>
<link href="https://fonts.googleapis.com/css2?family=Poppins:wght@400;500;600;700&display=swap" rel="stylesheet">
<style>
:root{
  --orange:#EE7325;
  --orange-2:#F08F49;
  --peach:#F5BC92;
  --cream:#FAE3D3;
  --ivory:#FDF4ED;
  --page:#111010;
  --card:#1a1716;
  --line:#3a3230;
  --muted:#9a8f88;
  --white:#ffffff;
}
*{box-sizing:border-box;margin:0;padding:0}
html,body{width:884px;height:1200px;overflow:hidden;background:#000;font-family:'Poppins',sans-serif;color:var(--white)}
.stage{position:absolute;left:0;top:0;width:1461px;height:1983px;transform:scale(0.60506);transform-origin:0 0}
.page{position:absolute;background:var(--page);overflow:hidden}
.page--home{left:3px;top:10px;width:720px;height:1958px;
  background:
    radial-gradient(ellipse 300px 220px at 360px 300px,rgba(110,55,20,.45),transparent 70%),
    radial-gradient(ellipse 380px 260px at 360px 1070px,rgba(100,50,20,.35),transparent 70%),
    radial-gradient(ellipse 380px 220px at 360px 1440px,rgba(100,50,20,.3),transparent 70%),
    var(--page)}
.page--market{left:737px;top:10px;width:720px;height:1000px;
  background:radial-gradient(ellipse 420px 420px at 360px 400px,rgba(100,50,20,.35),transparent 70%),var(--page)}
.abs{position:absolute}
.nav-logo{position:absolute;top:12px;width:24px;height:24px;border-radius:50%;background:var(--orange-2)}
.nav{position:absolute;top:19px;display:flex;gap:15px;font-size:9px}
.nav a{color:var(--white);text-decoration:none}
.nav a.active{color:var(--orange);text-decoration:underline}
.h-title{color:var(--orange);font-weight:600;font-size:22px;line-height:30px}
.center{text-align:center}
.sub{font-size:10px;line-height:16px;color:#e8e1dc}
.btn{display:inline-flex;align-items:center;gap:4px;height:22px;padding:0 10px;border-radius:3px;font-size:8.5px;background:var(--orange);color:var(--white);border:1px solid var(--orange)}
.btn--ghost{background:transparent;color:var(--orange-2)}
.img-fill{position:absolute}
/* hero */
.hero-car{left:318px;top:68px;width:402px;height:262px;
  background:radial-gradient(ellipse 60% 45% at 60% 55%,#e8722c 0%,#c45a22 35%,#6b3418 65%,transparent 80%);}
/* features */
.features{left:39px;top:457px;width:648px;height:331px;border-radius:18px;overflow:hidden;
  background:linear-gradient(100deg,#1e3a38 0%,#2b4b47 30%,#182826 55%,#2a3836 75%,#0e1413 100%)}
.feature-box{position:absolute;background:rgba(20,16,14,.88);padding:28px 22px}
.feature-box h3{color:var(--orange);font-size:20px;font-weight:600;margin-bottom:8px}
.feature-box p{font-size:11px;line-height:16px}
.divider{position:absolute;top:0;width:6px;height:100%;background:#3a2418}
/* card */
.card{position:absolute;width:156px;height:199px;border-radius:8px;background:linear-gradient(180deg,#242020,#161414);overflow:hidden}
.card h4{position:absolute;left:14px;top:19px;font-size:12px;font-weight:500}
.card .model{position:absolute;left:14px;top:39px;font-size:8px;color:var(--muted)}
.card .car{position:absolute;left:30px;top:58px;width:100px;height:44px;border-radius:40% 50% 20% 20%;
  background:radial-gradient(ellipse at 50% 55%,#f07a30,#c85d22 50%,transparent 75%)}
.specs{position:absolute;left:14px;top:121px;font-size:6.5px;display:grid;grid-template-columns:50px 60px;row-gap:7px}
.specs span{display:flex;align-items:center;gap:3px}
.specs svg{width:8px;height:8px}
.price{position:absolute;left:14px;bottom:18px;font-size:10px;font-weight:500}
.cart{position:absolute;right:0;bottom:0;width:34px;height:28px;background:var(--orange);border-radius:6px 0 8px 0;display:flex;align-items:center;justify-content:center}
.price-bar{position:absolute;left:0;bottom:0;width:100%;height:28px;background:var(--orange);border-radius:6px;display:flex;align-items:center;justify-content:center;font-size:10px;font-weight:500}
/* blog */
.blog-img{position:absolute;top:1334px;width:213px;height:146px;border-radius:6px;
  background:radial-gradient(ellipse at 50% 45%,#7a6555,#3e322b 55%,#1b1512 100%)}
.pill{position:absolute;left:6px;top:8px;background:var(--orange-2);font-size:8px;padding:1px 8px;border-radius:8px}
.corner{position:absolute;right:6px;top:6px;width:13px;height:13px;border-radius:3px;background:var(--peach)}
.blog-title{position:absolute;top:1489px;width:213px;text-align:center;font-size:8.5px;font-weight:600}
.brand{position:absolute;top:1585px;width:22px;height:22px;border-radius:50%;border:1.5px solid #666}
/* footer */
.foot-col h5{font-size:10px;font-weight:600;margin-bottom:10px}
.foot-col p{font-size:8px;margin-bottom:8px}
.foot-col{position:absolute}
.hr{position:absolute;left:0;width:100%;height:1px;background:#3a3a3a}
.social{display:flex;gap:7px;position:absolute}
.social i{display:block;width:17px;height:17px;border:1px solid #ccc;border-radius:3px}
.copy{position:absolute;width:100%;text-align:center;font-size:6.5px}
.select{position:absolute;top:165px;height:21px;border:1px solid #aaa;border-radius:3px;font-size:6.5px;display:flex;align-items:center;justify-content:space-between;padding:0 6px}
</style>
</head>
<body>
<svg width="0" height="0" style="position:absolute">
  <defs>
    <symbol id="i-clock" viewBox="0 0 10 10"><circle cx="5" cy="5" r="4" fill="none" stroke="#fff"/><path d="M5 2.5V5h2" fill="none" stroke="#fff"/></symbol>
    <symbol id="i-speed" viewBox="0 0 10 10"><rect x="1" y="1" width="8" height="8" fill="none" stroke="#fff"/><path d="M2.5 7l2-2 1.5 1.5L8 3" fill="none" stroke="#fff"/></symbol>
    <symbol id="i-fuel" viewBox="0 0 10 10"><rect x="1" y="1.5" width="5" height="7" fill="none" stroke="#fff"/><path d="M6 4h2v4" fill="none" stroke="#fff"/></symbol>
    <symbol id="i-cart" viewBox="0 0 10 10"><path d="M2 2.5h6l-.6 6H2.6z M3.5 4.5a1.5 1.5 0 0 0 3 0" fill="none" stroke="#fff" stroke-width=".9"/></symbol>
    <symbol id="i-arrow" viewBox="0 0 10 10"><path d="M3.5 2l3 3-3 3" fill="none" stroke="#fff" stroke-width="1.3"/></symbol>
    <symbol id="i-search" viewBox="0 0 10 10"><circle cx="4.3" cy="4.3" r="3" fill="none" stroke="#fff"/><path d="M6.5 6.5L9 9" stroke="#fff"/></symbol>
    <symbol id="i-chev" viewBox="0 0 10 10"><path d="M2.5 4l2.5 2.5L7.5 4" fill="none" stroke="#fff"/></symbol>
  </defs>
</svg>

<div class="stage">

<!-- ============ HOME PAGE ============ -->
<section class="page page--home">
  <div class="nav-logo" style="left:35px" aria-label="Brimble Diecast"></div>
  <nav class="nav" style="right:40px"><a class="active">Home</a><a>Marketplace</a><a>Community</a></nav>

  <h1 class="h-title abs" style="left:36px;top:88px;width:230px">Where Collectors Connect</h1>
  <p class="abs" style="left:36px;top:165px;width:215px;font-size:11px;line-height:18.5px">Welcome to the ultimate hub for diecast collectors. Explore a growing marketplace where you can buy, sell, or trade your favorite models with collectors from around the world.</p>
  <div class="abs" style="left:36px;top:273px;display:flex;gap:6px">
    <span class="btn">Browse Models <svg width="8" height="8"><use href="#i-arrow"/></svg></span>
    <span class="btn btn--ghost">Sell your collection</span>
  </div>
  <div class="img-fill hero-car" role="img" aria-label="Cream and orange vintage sedan model car"></div>

  <h2 class="h-title abs center" style="left:0;top:365px;width:720px">Why Choose Brimble Diecast ?</h2>
  <p class="sub abs center" style="left:160px;top:398px;width:400px">We bring together passionate collectors and high-quality diecast cars in one trusted space.</p>

  <div class="features abs" role="img" aria-label="Teal classic cars in a dark studio">
    <div class="divider" style="left:216px"></div>
    <div class="divider" style="left:426px"></div>
    <div class="feature-box" style="left:0;top:0;width:216px;height:191px">
      <h3>Buy &amp; Sell</h3>
      <p>Discover verified listings from collectors worldwide. Each listing includes detailed descriptions and photos so you can shop with confidence.</p>
      <span class="btn" style="margin-top:10px;height:20px">Buy &amp; Sell</span>
    </div>
    <div class="feature-box" style="left:222px;top:160px;width:204px;height:171px;padding-top:10px">
      <h3>Trade</h3>
      <p>Connect with other collectors and trade models securely through our built-in messaging and trade-offer system.</p>
      <span class="btn" style="margin-top:10px;height:20px">Trade</span>
    </div>
    <div class="feature-box" style="left:432px;top:0;width:216px;height:201px">
      <h3>Commmunity</h3>
      <p>Join a community of diecast enthusiasts who share your passion. Post your collection, discuss rare finds, and stay updated.</p>
      <span class="btn" style="margin-top:10px;height:20px">Community</span>
    </div>
  </div>

  <h2 class="h-title abs center" style="left:0;top:841px;width:720px">Featured Models</h2>
  <p class="sub abs center" style="left:190px;top:874px;width:340px">Curated selection of high-quality diecast cars ready for their next collector</p>

  <div class="card" style="left:31px;top:948px"><h4>Varenne</h4><span class="model">Strada S</span><div class="car" role="img" aria-label="Orange model car"></div>
    <div class="specs"><span><svg><use href="#i-clock"/></svg>3.7 Sec</span><span><svg><use href="#i-speed"/></svg>356 Km/h</span><span><svg><use href="#i-fuel"/></svg>Diesel</span></div>
    <span class="price">$175,90</span><span class="cart"><svg width="11" height="11"><use href="#i-cart"/></svg></span></div>
  <div class="card" style="left:198px;top:948px"><h4>Varenne</h4><span class="model">Volta</span><div class="car" role="img" aria-label="Orange model car"></div>
    <div class="specs"><span><svg><use href="#i-clock"/></svg>3.7 Sec</span><span><svg><use href="#i-speed"/></svg>356 Km/h</span><span><svg><use href="#i-fuel"/></svg>Diesel</span></div>
    <span class="price">$114,90</span><span class="cart"><svg width="11" height="11"><use href="#i-cart"/></svg></span></div>
  <div class="card" style="left:366px;top:948px"><h4>Varenne</h4><span class="model">Strada S Cross</span><div class="car" role="img" aria-label="Orange model car"></div>
    <div class="specs"><span><svg><use href="#i-clock"/></svg>3.7 Sec</span><span><svg><use href="#i-speed"/></svg>356 Km/h</span><span><svg><use href="#i-fuel"/></svg>Diesel</span></div>
    <span class="price">$175,90</span><span class="cart"><svg width="11" height="11"><use href="#i-cart"/></svg></span></div>
  <div class="card" style="left:533px;top:948px"><h4>Varenne</h4><span class="model">Strada S Cross</span><div class="car" role="img" aria-label="Orange model car"></div>
    <div class="specs"><span><svg><use href="#i-clock"/></svg>3.7 Sec</span><span><svg><use href="#i-speed"/></svg>356 Km/h</span><span><svg><use href="#i-fuel"/></svg>Diesel</span></div>
    <span class="price">$175,90</span><span class="cart"><svg width="11" height="11"><use href="#i-cart"/></svg></span></div>

  <span class="btn abs" style="left:309px;top:1178px;height:24px">View All Models <svg width="8" height="8"><use href="#i-arrow"/></svg></span>

  <h2 class="h-title abs center" style="left:0;top:1244px;width:720px">Latest from the Blog</h2>
  <p class="sub abs center" style="left:250px;top:1277px;width:220px">Tips, guides, and stories from the diecast world.</p>

  <div class="blog-img" style="left:31px" role="img" aria-label="Vintage cars parked in an old garage"><span class="pill">Article</span><span class="corner"></span></div>
  <div class="blog-img" style="left:253px" role="img" aria-label="Vintage cars parked in an old garage"><span class="pill">Article</span><span class="corner"></span></div>
  <div class="blog-img" style="left:475px" role="img" aria-label="Vintage cars parked in an old garage"><span class="pill">Article</span><span class="corner"></span></div>
  <p class="blog-title" style="left:31px">Top 10 Rare Diecast Cars</p>
  <p class="blog-title" style="left:253px">Beginner's Guide to Collecting</p>
  <p class="blog-title" style="left:475px">How to store diecast cars</p>

  <span class="btn abs" style="left:315px;top:1525px;height:24px">See All Blogs <svg width="8" height="8"><use href="#i-arrow"/></svg></span>

  <span class="brand" style="left:42px"></span>
  <span class="brand" style="left:164px"></span>
  <span class="brand" style="left:287px"></span>
  <span class="brand" style="left:410px"></span>
  <span class="brand" style="left:533px"></span>
  <span class="brand" style="left:656px"></span>

  <div class="abs" style="left:0;top:1635px;width:720px;height:150px;border:1px solid #3a3a3a;text-align:center;padding-top:24px">
    <h2 style="font-size:22px;font-weight:600">Ready to Start Your Collection?</h2>
    <p class="sub" style="font-size:8.5px;width:380px;margin:8px auto 0">Browse our inventory, list your own cars, or connect with fellow enthusiasts — your next great find is waiting.</p>
    <div style="display:flex;gap:6px;justify-content:center;margin-top:12px">
      <span class="btn">Browse Models</span><span class="btn btn--ghost">Sell your collection</span>
    </div>
  </div>

  <div class="hr" style="top:1795px"></div>
  <div class="nav-logo" style="left:50px;top:1812px" aria-label="Brimble Diecast"></div>
  <p class="abs" style="left:50px;top:1850px;width:160px;font-size:8px;line-height:16px">The ultimate marketplace for diecast car enthusiasts to buy, sell, and trade with ease.</p>
  <div class="foot-col" style="left:311px;top:1812px"><h5>Shop</h5><p>Browse Inventory</p><p>Rare Finds</p><p>New Arrivals</p></div>
  <div class="foot-col" style="left:438px;top:1812px"><h5>Community</h5><p>Trade board</p><p>Showcase</p><p>Blogs</p></div>
  <div class="foot-col" style="left:574px;top:1812px"><h5>Support</h5><p>Help Centre</p><p style="margin-top:13px">Seller Guide</p></div>
  <div class="hr" style="top:1925px"></div>
  <p class="copy" style="top:1939px">© 2025 Brimble Diecast. All rights reserved.</p>
  <div class="social" style="left:622px;top:1934px"><i></i><i></i><i></i></div>
</section>

<!-- ============ MARKETPLACE PAGE ============ -->
<section class="page page--market">
  <div class="nav-logo" style="left:36px" aria-label="Brimble Diecast"></div>
  <nav class="nav" style="right:34px"><a>Home</a><a class="active">Market Place</a><a>Community</a></nav>

  <h1 class="h-title abs center" style="left:0;top:66px;width:720px">Buy, Sell &amp; Trade Diecast Cars</h1>
  <p class="sub abs center" style="left:170px;top:103px;width:380px;font-size:8.5px">A trusted marketplace where collectors can buy rare models, sell collections, and trade with confidence.</p>

  <div class="abs" style="left:0;top:156px;width:720px;height:39px;border-top:1px solid #3a3a3a;border-bottom:1px solid #3a3a3a;background:rgba(0,0,0,.25)"></div>
  <div class="select" style="left:36px;width:180px;border-radius:6px;justify-content:flex-start;gap:5px"><svg width="8" height="8"><use href="#i-search"/></svg>Kessler</div>
  <div class="select" style="left:377px;width:86px">Buy<svg width="8" height="8"><use href="#i-chev"/></svg></div>
  <div class="select" style="left:488px;width:86px">Featured<svg width="8" height="8"><use href="#i-chev"/></svg></div>
  <div class="select" style="left:598px;width:86px">All Condition<svg width="8" height="8"><use href="#i-chev"/></svg></div>

  <p class="abs" style="left:36px;top:216px;font-size:9px">Showing 8 results</p>

  <div class="card" style="left:31px;top:244px"><h4>Varenne</h4><span class="model">Strada S</span><div class="car" role="img" aria-label="Orange model car"></div>
    <div class="specs"><span><svg><use href="#i-clock"/></svg>3.7 Sec</span><span><svg><use href="#i-speed"/></svg>356 Km/h</span><span><svg><use href="#i-fuel"/></svg>Diesel</span></div><div class="price-bar">$175,90</div></div>
  <div class="card" style="left:198px;top:244px"><h4>Varenne</h4><span class="model">Volta</span><div class="car" role="img" aria-label="Orange model car"></div>
    <div class="specs"><span><svg><use href="#i-clock"/></svg>3.7 Sec</span><span><svg><use href="#i-speed"/></svg>356 Km/h</span><span><svg><use href="#i-fuel"/></svg>Diesel</span></div><div class="price-bar">$175,90</div></div>
  <div class="card" style="left:366px;top:244px"><h4>Varenne</h4><span class="model">Strada S Cross</span><div class="car" role="img" aria-label="Orange model car"></div>
    <div class="specs"><span><svg><use href="#i-clock"/></svg>3.7 Sec</span><span><svg><use href="#i-speed"/></svg>356 Km/h</span><span><svg><use href="#i-fuel"/></svg>Diesel</span></div><div class="price-bar">$175,90</div></div>
  <div class="card" style="left:533px;top:244px"><h4>Varenne</h4><span class="model">Volta</span><div class="car" role="img" aria-label="Orange model car"></div>
    <div class="specs"><span><svg><use href="#i-clock"/></svg>3.7 Sec</span><span><svg><use href="#i-speed"/></svg>356 Km/h</span><span><svg><use href="#i-fuel"/></svg>Diesel</span></div><div class="price-bar">$175,90</div></div>

  <div class="card" style="left:31px;top:459px"><h4>Varenne</h4><span class="model">Volta</span><div class="car" role="img" aria-label="Orange model car"></div>
    <div class="specs"><span><svg><use href="#i-clock"/></svg>3.7 Sec</span><span><svg><use href="#i-speed"/></svg>356 Km/h</span><span><svg><use href="#i-fuel"/></svg>Diesel</span></div><div class="price-bar">$175,90</div></div>
  <div class="card" style="left:198px;top:459px"><h4>Varenne</h4><span class="model">Volta</span><div class="car" role="img" aria-label="Orange model car"></div>
    <div class="specs"><span><svg><use href="#i-clock"/></svg>3.7 Sec</span><span><svg><use href="#i-speed"/></svg>356 Km/h</span><span><svg><use href="#i-fuel"/></svg>Diesel</span></div><div class="price-bar">$175,90</div></div>
  <div class="card" style="left:366px;top:459px"><h4>Varenne</h4><span class="model">Strada S Cross</span><div class="car" role="img" aria-label="Orange model car"></div>
    <div class="specs"><span><svg><use href="#i-clock"/></svg>3.7 Sec</span><span><svg><use href="#i-speed"/></svg>356 Km/h</span><span><svg><use href="#i-fuel"/></svg>Diesel</span></div><div class="price-bar">$175,90 <svg width="10" height="10" style="position:absolute;right:10px"><use href="#i-cart"/></svg></div></div>
  <div class="card" style="left:533px;top:459px"><h4>Varenne</h4><span class="model">Volta</span><div class="car" role="img" aria-label="Orange model car"></div>
    <div class="specs"><span><svg><use href="#i-clock"/></svg>3.7 Sec</span><span><svg><use href="#i-speed"/></svg>356 Km/h</span><span><svg><use href="#i-fuel"/></svg>Diesel</span></div><div class="price-bar">$175,90</div></div>

  <div class="hr" style="top:828px"></div>
  <div class="nav-logo" style="left:51px;top:845px" aria-label="Brimble Diecast"></div>
  <p class="abs" style="left:51px;top:882px;width:160px;font-size:8px;line-height:16px">The ultimate marketplace for diecast car enthusiasts to buy, sell, and trade with ease.</p>
  <div class="foot-col" style="left:311px;top:845px"><h5>Shop</h5><p>Browse Inventory</p><p>Rare Finds</p><p>New Arrivals</p></div>
  <div class="foot-col" style="left:439px;top:845px"><h5>Community</h5><p>Trade board</p><p>Showcase</p><p>Blogs</p></div>
  <div class="foot-col" style="left:575px;top:845px"><h5>Support</h5><p>Help Centre</p><p style="margin-top:13px">Seller Guide</p></div>
  <div class="hr" style="top:958px"></div>
  <p class="copy" style="top:972px">© 2025 Brimble Diecast. All rights reserved.</p>
  <div class="social" style="left:623px;top:968px"><i></i><i></i><i></i></div>
</section>

</div>
</body>
</html>
```